Webdesign for Dutch IT consultancy company

Make a Wordpress webdesign for a Dutch consultancy company

Briefing Velmora IT

Website for finding and connecting IT-professionals. Corebusiness is to find IT-professionals and to help them to follow their ambitions. We offer training, personal coaching and education trajects.

U can take www.Tralvique.nl as an example for the website.

Home page

U can take www.Tralvique.nl as an example.

There should be jobs on the home page. A block for short info about us and about what whe do and a trigger to contact us quickly.

Jobs Page

On this page should be the jobs that we offer for the professionals. There should be a search function on this page so u can easily find the job that you are looking for.

A call to action can be on this page too.

Also a little block with text for some information.

For professionals page

Block with information on top. Call to action. info about who we work for/with.

For Clients

Info about three different solutions

- Sourcing solutions
- Consultancy solutions
- Custom based traineeships

Request a qoute option

Traineeships page

Info about two different traineeships

- Kernix traineeships
- Wintara traineeships

Call to action/ subscribe for traineeships

About us page

We are Velmora IT

Our mission: Creating cooperations between young professionals and businesses who wanna work on a great future.

Our core values

Last news

Target Market(s)

Young professionals and businesses who need IT services

Industry/Entity Type

It Company

Coding

Coded - Design and coding required

Number of Pages Required

5+ page

Font styles to use
Other font styles liked:
• Calibri

Colors
ffffff
add136
6b449b

Requirements
Must have
• Home page, Jobs Page, Professionals page, Clients page, Traineeships page, About us Page
• Green and/or Purple layout. Job search option, subscribe option
Nice to have
• modern design

```html
<!DOCTYPE html>
<html lang="en">
<head>
<meta charset="utf-8">
<title>Velmora IT – Sourcing | Consultancy</title>
<link href="https://fonts.googleapis.com/css2?family=Lato:ital,wght@0,400;0,700;0,900;1,400&display=swap" rel="stylesheet">
<style>
:root{
  --purple:#6b449b;
  --purple-deep:#4e2a7a;
  --green:#add136;
  --green-dark:#8fb21f;
  --black:#0d0d0d;
  --ink:#222;
  --muted:#777;
  --line:#e3e3e3;
  --white:#fff;
}
*{box-sizing:border-box;margin:0;padding:0}
html,body{width:1200px;height:3789px;overflow:hidden}
body{font-family:"Lato",Arial,sans-serif;color:var(--ink);background:var(--white);position:relative}
p{line-height:1.75}
.btn{display:inline-block;background:var(--green);color:var(--white);font-weight:700;font-size:20px;text-transform:uppercase;padding:14px 30px;letter-spacing:.5px}
.section-title{font-weight:900;font-size:42px;text-transform:uppercase;color:var(--purple);text-align:center}
.title-rule{width:340px;height:2px;background:var(--line);margin:18px auto 0;position:relative}
.title-rule::after{content:"";position:absolute;left:120px;top:0;width:100px;height:2px;background:var(--purple)}

/* header */
.topbar{position:absolute;top:0;left:0;width:1200px;height:96px;background:var(--black)}
.brand{position:absolute;left:76px;top:20px;color:var(--purple);font-weight:900;font-size:42px;letter-spacing:1px;line-height:1}
.brand small{display:block;color:#ccc;font-size:11px;font-weight:400;letter-spacing:4px;margin-top:4px;text-align:center}
.callus{position:absolute;right:76px;top:16px;display:flex;align-items:center;gap:16px;color:var(--white)}
.callus span{display:block;font-size:16px}
.callus strong{display:block;color:var(--green);font-size:32px;font-weight:700}
.nav{position:absolute;top:96px;left:0;width:1200px;height:61px;background:var(--white);border-bottom:1px solid var(--line)}
.nav ul{position:absolute;left:76px;top:0;display:flex;list-style:none;height:61px}
.nav li{font-size:16px;text-transform:uppercase;line-height:61px;padding:0 25px;color:#333;white-space:nowrap}
.nav li.active{background:var(--green);color:var(--white)}
.nav .search{position:absolute;right:76px;top:19px}

/* hero */
.hero{position:absolute;top:157px;left:0;width:1200px;height:520px}
.hero-photo{position:absolute;inset:0;background:linear-gradient(90deg,#c9c3c7 0%,#e8e4e6 40%,#c6b6d2 75%,#a68cc0 100%)}
.job-form{position:absolute;left:702px;top:15px;width:422px;height:490px;background:rgba(232,226,238,.92)}
.job-form h2{font-weight:900;font-size:32px;color:var(--purple);text-align:center;padding:22px 0 14px;border-bottom:2px solid rgba(107,68,155,.3);margin:0 0 30px}
.field{margin:0 30px 14px;height:44px;background:var(--white);font-size:13px;color:#999;line-height:44px;padding:0 16px;position:relative}
.field i{position:absolute;right:14px;top:15px;width:14px;height:14px;background:#777;border-radius:2px}
.job-form .btn{display:block;width:210px;margin:26px auto 0;text-align:center;font-size:20px}
.dots{position:absolute;left:555px;bottom:18px;display:flex;gap:10px}
.dots i{width:14px;height:14px;border-radius:50%;background:var(--white)}
.dots i:last-child{background:var(--green)}

/* solutions */
.solutions{position:absolute;top:677px;left:0;width:1200px;height:493px}
.solutions .section-title{margin-top:60px}
.sol{position:absolute;top:160px;width:300px;text-align:center}
.sol svg{display:block;margin:0 auto 18px}
.sol h3{font-size:17px;font-weight:700;text-transform:uppercase;margin-bottom:14px}
.sol p{font-size:14px;color:var(--muted)}
.sol .arrow{margin-top:12px}

/* welcome */
.welcome{position:absolute;top:1170px;left:0;width:1200px;height:417px;background:linear-gradient(90deg,#6a3f9a,#8d5cb8 50%,#6b449b);color:var(--white);text-align:center}
.welcome h2{font-weight:900;font-size:40px;text-transform:uppercase;margin-top:70px}
.welcome h4{font-size:19px;font-weight:700;width:820px;margin:30px auto 0;line-height:1.5}
.welcome p{font-size:14px;width:880px;margin:12px auto 0;line-height:1.9}
.welcome .btn{margin-top:18px}

/* what we do */
.what{position:absolute;top:1587px;left:0;width:1200px;height:479px}
.what h2{position:absolute;left:76px;top:55px;font-weight:900;font-size:40px;color:var(--purple)}
.what .rule{position:absolute;left:76px;top:116px;width:560px;height:2px;background:var(--line)}
.what .rule::after{content:"";position:absolute;left:0;width:100px;height:2px;background:var(--purple)}
.what .text{position:absolute;left:76px;top:150px;width:556px;font-size:14px;color:var(--muted)}
.what .text p+p{margin-top:12px}
.what .btn{position:absolute;left:76px;top:338px}
.what-photo{position:absolute;left:720px;top:70px;width:404px;height:360px;background:radial-gradient(ellipse at 60% 50%,#d8e0ea 0%,#eef1f5 55%,#fff 80%)}

/* traineeships */
.trainee{position:absolute;top:2066px;left:0;width:1200px;height:586px;background:linear-gradient(90deg,#8dbb2a,#b4d64a 50%,#9cc434);text-align:center}
.trainee .section-title{margin-top:52px}
.trainee .title-rule{background:rgba(255,255,255,.4)}
.trainee .lead{font-style:italic;font-size:18px;color:var(--white);margin-top:34px}
.trainee .call{font-weight:700;font-size:32px;color:var(--black);margin-top:12px}
.track{position:absolute;top:300px;width:270px;font-size:14px;color:var(--white)}
.track h3{color:var(--purple);font-weight:900;font-size:19px;text-transform:uppercase;margin-bottom:6px}
.track.left{left:76px;text-align:right}
.track.right{left:848px;text-align:left}
.badge{position:absolute;top:300px;width:106px;height:106px;border-radius:50%;background:var(--white);border:6px solid var(--purple)}

/* news */
.news{position:absolute;top:2652px;left:0;width:1200px;height:581px}
.news .section-title{margin-top:60px}
.card{position:absolute;top:165px;width:323px}
.card .ph{height:206px;background:linear-gradient(135deg,#c9d3dd,#8a9aab 60%,#5f6f80);position:relative}
.date{position:absolute;left:0;bottom:22px;width:54px;height:68px;background:var(--green);color:var(--white);text-align:center;font-weight:700;font-size:30px;line-height:1.4}
.date small{display:block;font-size:11px;line-height:1}
.card h4{font-size:16px;font-weight:700;margin-top:18px;white-space:nowrap}
.card p{font-size:14px;color:var(--muted);margin-top:8px;padding-bottom:16px;border-bottom:1px solid var(--line)}
.meta{display:flex;gap:34px;font-size:13px;margin-top:16px}
.meta span::before{content:"";display:inline-block;width:12px;height:12px;border-radius:50%;background:var(--green);margin-right:8px;vertical-align:-1px}

/* testimonial */
.quote{position:absolute;top:3233px;left:0;width:1200px;height:177px;background:var(--purple);color:var(--white)}
.quote .avatar{position:absolute;left:98px;top:30px;width:118px;height:118px;border-radius:50%;border:4px solid var(--white);background:linear-gradient(160deg,#e3d6cf,#9a7d70)}
.quote .bar{position:absolute;left:256px;top:30px;width:2px;height:118px;background:rgba(255,255,255,.3)}
.quote p{position:absolute;left:290px;top:24px;width:820px;font-size:14px;font-style:italic;line-height:2}
.quote .who{position:absolute;right:100px;top:136px;font-size:15px;color:var(--green);text-transform:uppercase}
.quote .who::before{content:"";display:inline-block;width:26px;height:2px;background:var(--green);margin-right:12px;vertical-align:4px}
.quote .chev{position:absolute;top:66px}

/* footer */
.footer{position:absolute;top:3410px;left:0;width:1200px;height:379px;background:var(--black);color:#ddd}
.footer .brand{top:96px}
.socials{position:absolute;left:120px;top:176px;display:flex;gap:18px}
.socials i{width:40px;height:40px;border-radius:50%;background:var(--green)}
.fcol{position:absolute;top:34px}
.fcol h5{color:var(--green);font-size:16px;font-weight:700;text-transform:uppercase;margin-bottom:14px}
.fcol ul{list-style:none;font-size:14px;line-height:26px}
.fcol li::before{content:"";display:inline-block;width:6px;height:6px;border-radius:50%;background:var(--green);margin-right:14px;vertical-align:2px}
.fcol p{font-size:14px;line-height:1.8}
.email-in{width:250px;height:44px;background:var(--white);color:#999;font-size:13px;line-height:44px;padding-left:14px;margin-top:14px}
.fcol .btn{margin-top:12px;font-size:18px;padding:12px 34px}
.contact-row{display:flex;gap:18px;font-size:14px;margin-top:12px}
.contact-row svg{flex:none}
.copyright{position:absolute;left:0;top:316px;width:1200px;height:63px;border-top:1px solid #333;text-align:center;line-height:63px;font-size:13px;color:#ccc}
</style>
</head>
<body>

<header class="topbar">
  <div class="brand">VELMORA IT<small>SOURCING | CONSULTANCY</small></div>
  <div class="callus">
    <svg width="40" height="40" viewBox="0 0 24 24"><path fill="#add136" d="M6.6 10.8a15 15 0 0 0 6.6 6.6l2.2-2.2c.3-.3.7-.4 1-.2 1.1.4 2.3.6 3.6.6.6 0 1 .4 1 1V20c0 .6-.4 1-1 1A17 17 0 0 1 3 4c0-.6.4-1 1-1h3.5c.6 0 1 .4 1 1 0 1.3.2 2.5.6 3.6.1.3 0 .7-.2 1z"/></svg>
    <div><span>Call Us Today :</span><strong>123 456 7890</strong></div>
  </div>
</header>

<nav class="nav">
  <ul>
    <li class="active">Home</li><li>About Us</li><li>Job</li><li>Professional</li><li>Clients</li><li>Traineeships</li><li>News</li><li>Contact Us</li>
  </ul>
  <svg class="search" width="22" height="22" viewBox="0 0 24 24"><circle cx="10" cy="10" r="7" fill="none" stroke="#6b449b" stroke-width="3"/><path d="M15 15l7 7" stroke="#6b449b" stroke-width="3"/></svg>
</nav>

<section class="hero">
  <div class="hero-photo" role="img" aria-label="Photo of a young professional woman with glasses thinking at her desk"></div>
  <form class="job-form">
    <h2>FIND A JOB</h2>
    <div class="field">Name *<i></i></div>
    <div class="field">Email *<i></i></div>
    <div class="field">Phone *<i></i></div>
    <div class="field">Select Job *<i></i></div>
    <div class="field">Resume *<i></i></div>
    <span class="btn">Submit</span>
  </form>
  <div class="dots"><i></i><i></i><i></i><i></i></div>
</section>

<section class="solutions">
  <h2 class="section-title">Our Best Solutions</h2>
  <div class="title-rule"></div>

  <div class="sol" style="left:95px">
    <svg width="100" height="100" viewBox="0 0 100 100" fill="none" stroke="#aaa" stroke-width="3"><rect x="14" y="10" width="50" height="66" rx="4"/><rect x="52" y="38" width="34" height="50" rx="4"/><path d="M24 26h30M24 38h20M24 50h20"/></svg>
    <h3>Sourcing Solutions</h3>
    <p>Lorem Ipsum is simply dummy text of the printing and typesetting industry. Lorem Ipsum has been.</p>
    <svg class="arrow" width="34" height="14" viewBox="0 0 34 14"><path d="M0 7h30M24 1l7 6-7 6" stroke="#add136" stroke-width="3" fill="none"/></svg>
  </div>

  <div class="sol" style="left:449px">
    <svg width="100" height="100" viewBox="0 0 100 100"><rect x="30" y="8" width="40" height="28" rx="3" fill="#add136"/><circle cx="24" cy="48" r="9" fill="#add136"/><circle cx="76" cy="48" r="9" fill="#add136"/><path d="M10 74q14-18 28 0zM62 74q14-18 28 0z" fill="#add136"/><rect x="8" y="76" width="84" height="8" fill="#add136"/></svg>
    <h3>Consultancy Solutions</h3>
    <p>Lorem Ipsum is simply dummy text of the printing and typesetting industry. Lorem Ipsum has been.</p>
    <svg class="arrow" width="34" height="14" viewBox="0 0 34 14"><path d="M0 7h30M24 1l7 6-7 6" stroke="#add136" stroke-width="3" fill="none"/></svg>
  </div>

  <div class="sol" style="left:790px">
    <svg width="100" height="100" viewBox="0 0 100 100" fill="none" stroke="#aaa" stroke-width="3"><path d="M52 12h30v76H52"/><path d="M52 12l16 8v68l-16-8z"/><path d="M10 50h34M34 40l10 10-10 10"/></svg>
    <h3>Custom Based Traineeships</h3>
    <p>Lorem Ipsum is simply dummy text of the printing and typesetting industry. Lorem Ipsum has been.</p>
    <svg class="arrow" width="34" height="14" viewBox="0 0 34 14"><path d="M0 7h30M24 1l7 6-7 6" stroke="#add136" stroke-width="3" fill="none"/></svg>
  </div>
</section>

<section class="welcome" role="img" aria-label="Purple tinted photo of professionals at work">
  <h2>Welcome to Velmora IT</h2>
  <h4>Creating cooperations between young professionals and businesses who wanna work on a great future.</h4>
  <p>Lorem Ipsum is simply dummy text of the printing and typesetting industry. Lorem Ipsum has been the industry's standard dummy text ever since the 1500s, when an unknown printer took a galley of type and scrambled it to make a type specimen book. It has survived not only five centuries, but also the leap into electronic typesetting.</p>
  <span class="btn">Learn More</span>
</section>

<section class="what">
  <h2>WHAT WE DO</h2>
  <div class="rule"></div>
  <div class="text">
    <p>Lorem Ipsum is simply dummy text of the printing and typesetting industry. Lorem Ipsum has been the industry's standard dummy text ever since the 1500s, when an unknown printer took a galley of type and scrambled.</p>
    <p>It was popularised in the 1960s with the release of Dravel sheets containing Lorem Ipsum passages, and more recently with desktop publishing software like Pressmo Layout including versions of Lorem Ipsum.</p>
  </div>
  <span class="btn">Learn More</span>
  <div class="what-photo" role="img" aria-label="Photo of a young man sitting cross-legged using a tablet"></div>
</section>

<section class="trainee" role="img" aria-label="Green tinted photo of hands working on a laptop">
  <h2 class="section-title">Our Traineeships</h2>
  <div class="title-rule"></div>
  <p class="lead">Lorem Ipsum is simply dummy text of the printing and typesetting industry.</p>
  <p class="call">Call Us Today -&nbsp; 123 456 7890</p>
  <div class="track left"><h3>Kernix Traineeship</h3><p>Lorem Ipsum is simply dummy text of the printing and typesetting industry. Lorem Ipsum has been.</p></div>
  <div class="badge" style="left:358px"></div>
  <div class="badge" style="left:728px"></div>
  <div class="track right"><h3>Wintara Traineeship</h3><p>Lorem Ipsum is simply dummy text of the printing and typesetting industry. Lorem Ipsum has been.</p></div>
</section>

<section class="news">
  <h2 class="section-title">Latest News</h2>
  <div class="title-rule"></div>

  <article class="card" style="left:76px">
    <div class="ph" role="img" aria-label="Photo of a business team meeting"><div class="date">15<small>DEC</small></div></div>
    <h4>Lorem Ipsum is simply dummy text of the</h4>
    <p>Lorem Ipsum is simply dummy text of the printing and typesetting industry.</p>
    <div class="meta"><span>by VELMORA IT</span><span>0 Comment</span></div>
  </article>
  <article class="card" style="left:437px">
    <div class="ph" role="img" aria-label="Photo of a businesswoman in an office"><div class="date">15<small>DEC</small></div></div>
    <h4>Lorem Ipsum is simply dummy text of the</h4>
    <p>Lorem Ipsum is simply dummy text of the printing and typesetting industry.</p>
    <div class="meta"><span>by VELMORA IT</span><span>0 Comment</span></div>
  </article>
  <article class="card" style="left:801px">
    <div class="ph" role="img" aria-label="Photo of colleagues working at a laptop"><div class="date">15<small>DEC</small></div></div>
    <h4>Lorem Ipsum is simply dummy text of the</h4>
    <p>Lorem Ipsum is simply dummy text of the printing and typesetting industry.</p>
    <div class="meta"><span>by VELMORA IT</span><span>0 Comment</span></div>
  </article>
</section>

<section class="quote">
  <svg class="chev" style="left:30px" width="20" height="44" viewBox="0 0 20 44"><path d="M18 2L3 22l15 20" stroke="#fff" stroke-width="2" fill="none"/></svg>
  <div class="avatar" role="img" aria-label="Portrait photo of the client"></div>
  <div class="bar"></div>
  <p>" Lorem Ipsum is simply dummy text of the printing and typesetting industry. Lorem Ipsum has been the industry's standard dummy text ever since the 1500s, when an unknown printer took a galley of type and scrambled. It was popularised in the 1960s with the release of Dravel sheets containing Lorem Ipsum passages"</p>
  <div class="who">Client Name</div>
  <svg class="chev" style="right:30px" width="20" height="44" viewBox="0 0 20 44"><path d="M2 2l15 20L2 42" stroke="#fff" stroke-width="2" fill="none"/></svg>
</section>

<footer class="footer">
  <div class="brand">VELMORA IT<small>SOURCING | CONSULTANCY</small></div>
  <div class="socials"><i></i><i></i><i></i></div>

  <div class="fcol" style="left:346px">
    <h5>Sitemap</h5>
    <ul><li>Home</li><li>About Us</li><li>Job</li><li>Professional</li><li>Clients</li><li>Trainership</li><li>News</li><li>Contact Us</li></ul>
  </div>

  <div class="fcol" style="left:606px;width:250px">
    <h5>Newsletter</h5>
    <p>Would you like to receive exclusive access to articles, white papers and our regular monthly newsletter?</p>
    <div class="email-in">Enter Email *</div>
    <span class="btn">Subscribe</span>
  </div>

  <div class="fcol" style="left:872px;width:252px">
    <h5>Contact Us</h5>
    <div class="contact-row">
      <svg width="20" height="26" viewBox="0 0 20 26"><path d="M10 0a9 9 0 0 1 9 9c0 7-9 17-9 17S1 16 1 9a9 9 0 0 1 9-9z" fill="#add136"/><circle cx="10" cy="9" r="3.5" fill="#0d0d0d"/></svg>
      <p><strong style="color:#fff">VELMORA IT</strong><br>101 - Lorem Ipsum is simple Dummy text of print and type industry text.</p>
    </div>
    <div class="contact-row">
      <svg width="20" height="20" viewBox="0 0 24 24"><path fill="#add136" d="M6.6 10.8a15 15 0 0 0 6.6 6.6l2.2-2.2c.3-.3.7-.4 1-.2 1.1.4 2.3.6 3.6.6.6 0 1 .4 1 1V20c0 .6-.4 1-1 1A17 17 0 0 1 3 4c0-.6.4-1 1-1h3.5c.6 0 1 .4 1 1 0 1.3.2 2.5.6 3.6.1.3 0 .7-.2 1z"/></svg>
      <p>123 456 7890</p>
    </div>
    <div class="contact-row">
      <svg width="20" height="16" viewBox="0 0 20 16"><rect width="20" height="16" rx="2" fill="#add136"/><path d="M1 2l9 7 9-7" stroke="#0d0d0d" stroke-width="1.6" fill="none"/></svg>
      <p>info@velmorait.com</p>
    </div>
  </div>

  <div class="copyright">©VELMORA IT SOLUTIONS | CONSULTANCY - 2017 All right Reserved.</div>
</footer>

</body>
</html>
```